Speisekarten für griechisches Restaurant
Zielgruppe
modernes griechisches Restaurant
Aufgabenstellung
neues modernen helles design ,
nach Durchsicht aus meinen Vorlangen, sollten ein paar Anpassung am text und preisen noch durchgeführt werden.
aus der pdf datei,, ist ab Seite 7 die richtige Speisekarte,, vorher sind nur entwürfe vom mir, diese bitte ignorieren.

```html
<!DOCTYPE html>
<html lang="de">
<head>
<meta charset="utf-8">
<title>Levanti – Speisekarte</title>
<link href="https://fonts.googleapis.com/css2?family=Barlow+Condensed:ital,wght@0,400;0,600;0,700;1,400&family=Damion&display=swap" rel="stylesheet">
<style>
  :root{
    --stage:#2b3a22;
    --paper:#ecece9;
    --ink:#1b1b1b;
    --olive:#7c9a30;
    --frame:#a3b27a;
    --band:#cfd8bd;
  }
  *{box-sizing:border-box;margin:0;padding:0}
  html,body{width:1200px;height:800px;overflow:hidden}
  body{background:var(--stage);font-family:"Barlow Condensed",sans-serif;color:var(--ink);position:relative}
  .page{position:absolute;top:145px;width:360px;height:510px;background:var(--paper);overflow:hidden}
  .page--cover{left:30px}
  .page--spirits{left:420px}
  .page--pans{left:810px}
  .frame{position:absolute;border:1px solid var(--frame)}
  .script{font-family:"Damion",cursive;font-weight:400}

  /* restaurant name */
  .brand{position:absolute;left:0;right:0;text-align:center;color:var(--olive);font-weight:600;letter-spacing:1px}
  .brand--cover{top:62px;font-size:30px}
  .brand--foot{bottom:14px;font-size:13px}

  /* cover */
  .page--cover .frame{left:26px;right:26px;top:34px;bottom:40px}
  .cover__sprig{position:absolute;left:40px;right:40px;top:128px;bottom:42px;
    background:radial-gradient(ellipse at 45% 55%,rgba(190,200,160,.45),rgba(236,236,233,0) 70%)}
  .cover__title{position:absolute;top:190px;left:0;right:0;text-align:center;font-size:64px}

  /* spirits */
  .page--spirits .frame{left:26px;right:26px;top:56px;bottom:56px}
  .page-title{position:absolute;top:4px;left:0;right:0;text-align:center;font-size:54px;line-height:1}
  .page-title small{display:block;font-size:18px;margin-top:-4px}
  .cols{position:absolute;left:30px;right:30px;top:86px;display:flex;gap:10px}
  .col{flex:1;text-align:center}
  .item{margin-bottom:9px}
  .item b{display:block;font-weight:700;font-size:10px;text-transform:uppercase;letter-spacing:.2px}
  .item i{display:block;font-size:8.5px;line-height:1.15}
  .col--plain .item{margin-bottom:8.5px}
  .page-foot{position:absolute;bottom:10px;left:14px;font-size:6.5px;width:190px;line-height:1.25}
  .deco{position:absolute;background:radial-gradient(ellipse,rgba(200,200,195,.5),rgba(236,236,233,0) 70%)}

  /* pans */
  .page--pans .frame{left:26px;right:26px;top:70px;bottom:98px}
  .dish{margin-bottom:13px}
  .dish b{display:block;font-weight:700;font-size:10.5px;text-transform:uppercase}
  .dish i{display:block;font-size:8px;line-height:1.2}
  .note{font-size:8px;line-height:1.3}
  .note b{font-weight:700}
  .band{position:absolute;left:22px;right:22px;bottom:70px;height:34px;background:var(--band);border:1px solid var(--frame);
    display:flex;align-items:center;justify-content:center;text-align:center;font-style:italic;font-size:9px;color:var(--olive);font-weight:600;padding:0 20px}
</style>
</head>
<body>

<section class="page page--cover">
  <div class="frame"></div>
  <div class="cover__sprig" role="img" aria-label="Feine Strichzeichnung eines Olivenzweigs als Hintergrundschmuck"></div>
  <p class="brand brand--cover">LEVANTI</p>
  <h1 class="cover__title script">Speisekarte</h1>
</section>

<section class="page page--spirits">
  <div class="frame"></div>
  <h2 class="page-title script">Spirituosen</h2>
  <div class="cols">
    <div class="col">
      <div class="item"><b>Aranciol - Spritz | 6,5</b><i>0,2l</i></div>
      <div class="item"><b>Hugo | 6,5</b><i>0,2l</i></div>
      <div class="item"><b>Wermut Bianco | 5,-</b><i>0,1l</i></div>
      <div class="item"><b>Bitter Rosso - Orange | 5,-</b><i>0,1l</i></div>
      <div class="item"><b>Longdrinks | 7,-</b><i>Wodka, Whiskey, Rum (4cl)<br>+ Mischgetränk<br>0,2l</i></div>
      <div class="item"><b>Hausschnaps Korb | 3,5</b><i>verschiedene „Exclusive Liköre“<br>und Spirituosen aus Griechenland.<br>Gerne beraten wir Sie bei<br>der Auswahl.<br>2cl</i></div>
      <div class="item"><b>Ouzo | 2,5</b><i>2cl</i></div>
      <div class="item"><b>Ouzo Lesvia | 14,-</b><i>Flasche 0,2l</i></div>
      <div class="item"><b>Tsipouro | 3,5</b><i>(mit Anis) 2cl</i></div>
    </div>
    <div class="col col--plain">
      <div class="item"><b>Melaxos 5* | 4,-</b></div>
      <div class="item"><b>Melaxos 7* | 5,-</b></div>
      <div class="item"><b>Melaxos 40 Jahre | 7,-</b></div>
      <div class="item"><b>Melaxos flambiert | 7,-</b></div>
      <div class="item"><b>Kräuterbitter | 3,-</b></div>
      <div class="item"><b>Amaro | 3,-<br>Fernet | 3,-</b></div>
      <div class="item"><b>Aquavit Nord | 3,-</b></div>
      <div class="item"><b>Kräuterlikör | 3,-</b></div>
      <div class="item"><b>Williams Christ | 3,-</b></div>
      <div class="item"><b>Irish Cream | 3,-</b></div>
      <div class="item"><b>Sambuca | 3,-</b></div>
      <div class="item"><b>Tequila | 3,-</b></div>
      <div class="item"><b>Leckerchen | 2,3</b></div>
      <div class="item"><b>Kumquat - Likör | 3,-</b></div>
      <div class="item"><b>Bananen - Likör | 3,-</b></div>
      <div class="item"><b>Masticha - Likör | 3,-</b></div>
    </div>
  </div>
  <div class="deco" style="right:22px;bottom:40px;width:110px;height:90px" role="img" aria-label="Zarte Zeichnung von Gläsern und Flaschen"></div>
  <p class="page-foot">Alle Preise in €</p>
  <p class="brand brand--foot">LEVANTI</p>
</section>

<section class="page page--pans">
  <div class="frame"></div>
  <h2 class="page-title script">Tiganakia<small>(Pfannengerichte)</small></h2>
  <div class="cols" style="top:104px">
    <div class="col">
      <div class="dish"><b>43. Melaxos | 21,5</b><i>Schweinefilet-Medaillons mit<br>frischen Champignons und<br>einer Sauce nach Wahl</i></div>
      <div class="dish"><i>Melaxos-/Pfeffer-Sauce<br>oder verfeinert mit Weißwein</i></div>
      <div class="dish"><b>44. Chef | 23,-</b><i>Verschiedene Fleischsorten in einer<br>Tomaten-Knoblauch-Sauce<br>mit Crème-Fraîche verfeinert</i></div>
      <div class="dish"><b>45. Skordo | 23,-</b><i>Verschiedene Fleischsorten<br>mit Paprika, Zwiebeln und Fetakäse</i></div>
      <p class="note">Diese Gerichte werden von<br><b>Salat und Patatakia</b> begleitet</p>
    </div>
    <div class="col">
      <div class="dish"><b>46. Galopoula | 21,5</b><i>Putengeschnetzeltes mit frischen<br>Champignons, verfeinert mit einer<br>pikanten Sauce</i></div>
      <div class="dish"><b>47. Mon Amour | 21,-</b><i>Hähnchenbrustfilet in einer<br>Spezial-Fetasauce</i></div>
      <div class="dish"><b>48. Naxos | 24,-</b><i>Rumpsteak, Schweine- und Putenfilet<br>in einer Spezial-Fetasauce<br>mit Zucchini und Auberginenwürfel</i></div>
      <p class="note">Diese Gerichte werden von<br><b>Salat und Reis</b> begleitet</p>
    </div>
  </div>
  <div class="band">Tiganaki ist ein traditionelles griechisches Gericht, das aus Fleisch, Gemüse und einer Sauce besteht.</div>
  <div class="deco" style="left:20px;bottom:20px;width:120px;height:60px" role="img" aria-label="Zarte Zeichnung von Gemüse"></div>
  <div class="deco" style="right:14px;bottom:16px;width:110px;height:70px" role="img" aria-label="Zarte Zeichnung einer Pfanne mit Gericht"></div>
  <p class="page-foot">Alle Preise in €. Änderungen mit Mehrwand werden mit einem Aufpreis berechnet.</p>
  <p class="brand brand--foot">LEVANTI</p>
</section>

</body>
</html>
```